TIMBER DECK COMPANY FLYER

We need a flyer design for a Timber Decking company, we specialise in timber decks, stairs, privacy screens, maintenance and pergolas. I have attatched some pictures which you can incorporate if you think they need cropping go for it. We offer amazing decks at affordable prices by qualified tradespeople.
My logo is a dull green I would like this to be changed to a more lime bright green please. Also my logo is too big I would like this logo halved in size please. And the colours in the brochure maybe a blackbackground with lime green and other colours you think will work. We will also beat any reputable Decking companies quote by 10%. Our decks add style, class, longjevity and practicality to any home. The final design should be modern and cutting edge.

Target Market(s)

home owners

Industry/Entity Type

It Company

Logo Text

CEDARLINE PATIO WORKS

Requirements
Must have
• DECKS
STAIRS
PERGOLAS
PRIVACY SCREENS
DECK MAINTENANCE

CONTACT-GORDON-0427158302

MUST HAVE LIKE US ON FRIENDSPACE LOGO

www.cedarlinepatioworks.com.au
Nice to have
• Please let me know if need more photos etc

```html
<!DOCTYPE html>
<html lang="en">
<head>
<meta charset="utf-8">
<title>Cedarline Patio Works – Flyer</title>
<link rel="stylesheet" href="https://fonts.googleapis.com/css2?family=Arimo:wght@400&family=Tinos:wght@400&display=swap">
<style>
  :root {
    --canvas: #e6dccb;
    --black: #0b0b0b;
    --lime: #8ee62a;
    --lime-soft: #b6f06a;
    --stone: #e9dfc8;
    --ink: #1c1c1c;
    --panel-grey: #7a7a7a;
    --white: #ffffff;
    --sans: "Arimo", Arial, sans-serif;
    --serif: "Tinos", "Times New Roman", serif;
  }
  * { margin: 0; padding: 0; box-sizing: border-box; }
  html, body { width: 1200px; height: 1000px; overflow: hidden; }
  body { background: var(--canvas); position: relative; font-family: var(--sans); }

  .flyer { position: absolute; background: var(--black); box-shadow: 0 2px 6px rgba(0,0,0,.25); }

  /* ---------- Front ---------- */
  .flyer--front { left: 60px; top: 73px; width: 518px; height: 668px; }
  .front-photo {
    position: absolute; left: 28px; top: 24px; width: 465px; height: 616px;
    background:
      linear-gradient(180deg, rgba(30,30,30,.9) 0%, rgba(30,30,30,0) 28%),
      linear-gradient(100deg, #123a33 0%, #1d4a42 38%, #d9ceb5 40%, #d9ceb5 60%, #7a2a16 62%, #5c1d10 100%);
  }
  .headline-box {
    position: absolute; left: 72px; top: 36px; width: 382px; height: 100px;
    background: rgba(0,0,0,.72);
  }
  .headline {
    position: absolute; left: 72px; top: 42px; width: 382px; text-align: center;
    font-family: var(--serif); color: var(--lime); font-size: 20px; line-height: 27px; letter-spacing: .5px;
  }
  .headline-rule { position: absolute; left: 74px; top: 96px; width: 362px; height: 2px; background: var(--lime); }
  .tagline {
    position: absolute; left: 72px; top: 101px; width: 382px; text-align: center;
    color: var(--lime-soft); font-size: 15.5px; letter-spacing: .4px;
  }
  .services { list-style: none; position: absolute; color: var(--lime); font-size: 17.5px; line-height: 26.8px; }
  .services li::before { content: "•"; margin-right: 7px; }
  .flyer--front .services { left: 35px; top: 289px; }
  .front-brand {
    position: absolute; left: 118px; top: 528px; display: flex; align-items: center; gap: 10px;
  }
  .brand-square { width: 18px; height: 18px; background: var(--lime); }
  .brand-name { font-size: 15px; color: var(--ink); letter-spacing: .3px; }
  .front-url {
    position: absolute; left: 0; width: 100%; top: 610px; text-align: center;
    color: var(--lime); font-size: 19.5px;
  }

  /* ---------- Back ---------- */
  .flyer--back { left: 632px; top: 270px; width: 520px; height: 670px; }
  .photo { position: absolute; outline: 2px solid var(--lime); }
  .photo--pool { left: 35px; top: 33px; width: 221px; height: 315px;
    background: linear-gradient(160deg, #1f3a1c 0%, #3e6a2c 35%, #7a3a22 55%, #4aa7c9 70%, #2f6a24 100%); }
  .photo--deck { left: 260px; top: 33px; width: 225px; height: 246px;
    background: linear-gradient(150deg, #4a2416 0%, #8a3d22 45%, #6e2c18 70%, #3f7e22 100%); }
  .photo--stairs { left: 35px; top: 351px; width: 221px; height: 228px;
    background: linear-gradient(90deg, #1f4a22 0%, #2e5a2c 30%, #b6895a 55%, #8d6540 100%); }
  .contact-band { position: absolute; left: 0; top: 0; width: 300px; height: 260px; }
  .contact-text {
    position: absolute; left: 20px; top: 72px; width: 200px; text-align: center;
    transform: rotate(-42deg); transform-origin: center;
    font-family: var(--serif); color: var(--lime); font-size: 17px; line-height: 24px; letter-spacing: .5px;
  }
  .flyer--back .services { left: 276px; top: 339px; font-size: 18px; }
  .back-brand {
    position: absolute; left: 265px; top: 520px; width: 225px; height: 58px;
    background: var(--panel-grey); display: flex; align-items: center; justify-content: center;
  }
  .back-brand .brand-name { font-size: 14px; }
  .social-like {
    position: absolute; left: 27px; top: 611px; width: 88px; height: 26px;
    background: var(--white); display: flex; align-items: center; justify-content: center;
    font-size: 9px; color: var(--ink);
  }
  .back-url { position: absolute; left: 129px; top: 613px; color: var(--lime); font-size: 19.5px; }
</style>
</head>
<body>

<section class="flyer flyer--front">
  <div class="front-photo" role="img" aria-label="Photo of a plunge pool with sandstone coping, red timber decking and sandstone retaining walls"></div>
  <div class="headline-box"></div>
  <h1 class="headline">STYLE, CLASS, LONGJEVITY<br>AND PRACTICALITY TO ANY HOME.</h1>
  <div class="headline-rule"></div>
  <p class="tagline">Amazing decks at affordable prices!</p>
  <ul class="services">
    <li>DECKS</li><li>STAIRS</li><li>PERGOLAS</li><li>PRIVACY SCREENS</li><li>DECK MAINTENANCE</li>
  </ul>
  <div class="front-brand">
    <span class="brand-square"></span>
    <span class="brand-name">CEDARLINE PATIO WORKS</span>
  </div>
  <p class="front-url">www.cedarlinepatioworks.com.au</p>
</section>

<section class="flyer flyer--back">
  <div class="photo photo--pool" role="img" aria-label="Photo of a timber pool deck with glass fencing among garden greenery"></div>
  <div class="photo photo--deck" role="img" aria-label="Photo of a close-up red hardwood deck with leafy plant"></div>
  <div class="photo photo--stairs" role="img" aria-label="Photo of timber garden stairs with handrail among tropical plants"></div>
  <svg class="contact-band" viewBox="0 0 300 260" aria-hidden="true">
    <polygon points="35,112 160,0 262,0 35,205" fill="#0b0b0b"/>
    <line x1="35" y1="112" x2="160" y2="0" stroke="#8ee62a" stroke-width="2"/>
    <line x1="35" y1="205" x2="262" y2="0" stroke="#8ee62a" stroke-width="2"/>
  </svg>
  <p class="contact-text">CONTACT<br>GORDON-0427158302</p>
  <ul class="services">
    <li>DECKS</li><li>STAIRS</li><li>PERGOLAS</li><li>PRIVACY SCREENS</li><li>DECK MAINTENANCE</li>
  </ul>
  <div class="back-brand"><span class="brand-name">CEDARLINE PATIO WORKS</span></div>
  <div class="social-like">Like us on Friendspace</div>
  <p class="back-url">www.cedarlinepatioworks.com.au</p>
</section>

</body>
</html>
```